Property Management business needs Business cards designed

We provide a premium property management service based in Sydney's Norther Beaches. We want people to feel confident in choosing us to manage their investment properties. We offer a much more personalized service than other estate agents.
We want a modern clean design. Something that shows confidence without being complicated.
Logo attached.

Target Market(s)

35-70yo Male and Female with strong property portfolios within Sydney's Norther Beaches

Industry/Entity Type

Property Management

Contact Information for Business Card

Address: Suite 7, 12-14 Kelvin Parade, Harlow NSW 2188
Two separate named cards.
Tom Ardley - 0491 570 118 tom@harbourvaleestates.com.au
Clara Dunmore - 0491 570 263 clara@harbourvaleestates.com.au

Requirements
Must have
• Business logo, name, number, address, email.

```html
<!DOCTYPE html>
<html lang="en">
<head>
<meta charset="utf-8">
<title>Harbourvale Estates – Tom Ardley</title>
<link rel="stylesheet" href="https://fonts.googleapis.com/css2?family=Montserrat:wght@400;600;700&family=Open+Sans:wght@600&display=swap">
<style>
  :root {
    --ink: #231f20;
    --text: #3d3b3c;
    --teal: #25909b;
    --teal-deep: #1e6a7b;
    --name-teal: #1f6b7d;
    --sand: #d0cdb8;
    --icon: #c9c4ae;
    --paper: #ffffff;
  }
  html, body {
    margin: 0;
    padding: 0;
    overflow: hidden;
    background: var(--paper);
  }
  .card {
    position: relative;
    width: 1200px;
    height: 741px;
    overflow: hidden;
    background: linear-gradient(135deg, #f6f6f6 0%, #ffffff 45%, #fbfbfb 100%);
  }
  .card__artwork {
    position: absolute;
    inset: 0;
    background: linear-gradient(160deg, var(--teal-deep) 0%, var(--teal) 50%, var(--sand) 100%);
    clip-path: polygon(822px 0, 1200px 0, 1200px 741px, 530px 741px, 940px 525px);
  }
  .brand {
    position: absolute;
    left: 57px;
    top: 145px;
    display: flex;
    align-items: center;
    gap: 18px;
  }
  .brand__dot {
    width: 22px;
    height: 22px;
    border-radius: 50%;
    background: var(--teal);
  }
  .brand__name {
    margin: 0;
    font-family: "Open Sans", Arial, sans-serif;
    font-weight: 600;
    font-size: 50px;
    letter-spacing: 0.5px;
    color: var(--ink);
    line-height: 1;
  }
  .person {
    position: absolute;
    left: 60px;
    top: 390px;
    font-family: "Montserrat", Arial, sans-serif;
  }
  .person__name {
    margin: 0 0 12px;
    font-weight: 700;
    font-size: 37px;
    letter-spacing: 0.5px;
    color: var(--name-teal);
    text-transform: uppercase;
  }
  .contact {
    list-style: none;
    margin: 0;
    padding: 0;
  }
  .contact__item {
    display: flex;
    align-items: flex-start;
    gap: 22px;
    color: var(--text);
  }
  .contact__item--strong {
    font-weight: 700;
    font-size: 34px;
    height: 46px;
    align-items: center;
  }
  .contact__item--address {
    margin-top: 30px;
    font-weight: 400;
    font-size: 30px;
    line-height: 43px;
  }
  .contact__icon {
    width: 28px;
    height: 28px;
    flex: none;
  }
  .contact__item--address .contact__icon {
    margin-top: 7px;
  }
</style>
</head>
<body>
<main class="card">
  <div class="card__artwork" role="img" aria-label="Decorative teal and sand graphic area"></div>

  <header class="brand">
    <span class="brand__dot"></span>
    <h1 class="brand__name">HARBOURVALE ESTATES</h1>
  </header>

  <section class="person">
    <h2 class="person__name">Tom Ardley</h2>
    <ul class="contact">
      <li class="contact__item contact__item--strong">
        <svg class="contact__icon" viewBox="0 0 28 28" aria-hidden="true">
          <circle cx="14" cy="14" r="12.5" fill="none" stroke="var(--icon)" stroke-width="2"/>
          <path d="M10 7.5c1 0 2 2.5 2 3.2s-1.2 1.2-1.2 1.8c0 1 2.6 3.8 3.8 3.8.6 0 1.1-1.2 1.8-1.2s3.2 1 3.2 2-1.6 2.6-2.8 2.6C12 19.7 8.3 16 8.3 11c0-1.3 .7-3.5 1.7-3.5z" fill="var(--icon)"/>
        </svg>
        <span>0491 570 118</span>
      </li>
      <li class="contact__item contact__item--strong">
        <svg class="contact__icon" viewBox="0 0 28 28" aria-hidden="true">
          <rect x="2" y="6" width="24" height="16" fill="var(--icon)"/>
          <path d="M2 6l12 9 12-9" fill="none" stroke="var(--paper)" stroke-width="1.6"/>
        </svg>
        <span>tom@harbourvaleestates.com.au</span>
      </li>
      <li class="contact__item contact__item--address">
        <svg class="contact__icon" viewBox="0 0 28 28" aria-hidden="true">
          <path d="M14 2c5 0 8 3.5 8 8 0 5-8 16-8 16S6 15 6 10c0-4.5 3-8 8-8z" fill="var(--icon)"/>
        </svg>
        <span>Suite 7,<br>12-14 Kelvin Parade,<br>Harlow NSW 2188</span>
      </li>
    </ul>
  </section>
</main>
</body>
</html>
```